Law Firm Ad

We need a magazine/auction program design for a Sacramento based law firm. Current need is for a school auction sponsorship. Ad must be 5 1/2 x 8 1/2 in high resolution (300 dpi) and in JPG or PDF format. A clean, modern, simple design is preferred.

Brisley Law Corporation provides general preventative employment advice to employers in avoiding litigation and has counseled businesses on cases involving employment law, unfair business practices and trade secrets. Brisley Law Corporation also practices in business, real estate and employment litigation.

Target Market(s)

This particular ad it is to support Hollowbrook Elementary School's 21st Annual Auction and Dinner on March 14, 2015.
Here's the facebook link https://www.examplesocial.net/HollowbrookAuction/photos/a.718204936051827.260319.709482615039471/2049361857402116/?type=1&theater
But I would like something that might be fairly universal.

Industry/Entity Type

Real Estate

Font styles to use
Sans Serif

Requirements
Must have
• Clean and crisp design. Not overly traditional.
Nice to have
• Contact information:
Brisley Law Corporation
388 Wexley Avenue, Suite 200
Sacramento, CA 95871
916.555.0147
brisley-law.example

```html
<!DOCTYPE html>
<html lang="en">
<head>
<meta charset="utf-8">
<title>Brisley Law Corporation – Program Ad</title>
<link rel="stylesheet" href="https://fonts.googleapis.com/css2?family=Jost:wght@300;500;600&display=swap">
<style>
  :root {
    --stage: #3a3a3a;
    --forest: #2c3a1c;
    --orange: #f47a20;
    --gold: #f7941d;
    --tan: #d8a15a;
    --ink: #3d4740;
    --brown: #3a1c0c;
    --white: #ffffff;
    --photo-dark: #26391a;
    --photo-mid: #4a6a2c;
    --photo-light: #e9e6dc;
  }
  * { box-sizing: border-box; margin: 0; padding: 0; }
  html, body { width: 1200px; height: 900px; overflow: hidden; }
  body {
    background: var(--stage);
    font-family: "Jost", "Futura", sans-serif;
    display: flex; align-items: center; justify-content: center;
  }
  .ad {
    position: relative;
    width: 560px; height: 866px;
    background: var(--forest);
    overflow: hidden;
  }
  .ad__cap {
    position: absolute; left: 0; right: 0; top: 0; height: 20px;
    background: var(--forest);
  }
  .ad__header {
    position: absolute; left: 0; right: 0; top: 20px; height: 182px;
    background: var(--white);
    border-top: 4px solid var(--gold);
    border-bottom: 5px solid var(--gold);
    display: flex; align-items: center; justify-content: center;
  }
  .brand-name {
    color: var(--gold);
    font-weight: 600;
    font-size: 58px;
    line-height: 1.02;
    text-align: center;
    letter-spacing: 0.5px;
  }
  .ad__photo {
    position: absolute; left: 0; right: 0; top: 202px; height: 548px;
    background:
      radial-gradient(ellipse 55% 60% at 70% 65%, var(--photo-light) 0%, #cfcabb 45%, rgba(74,106,44,0) 75%),
      linear-gradient(160deg, var(--photo-mid) 0%, var(--photo-dark) 100%);
  }
  .headline {
    position: absolute; left: 13px; top: 222px;
    color: var(--white);
    font-weight: 300;
    font-size: 22px;
    line-height: 30px;
  }
  .headline strong { font-weight: 500; }
  .headline .accent { color: var(--tan); font-weight: 500; }
  .contact {
    position: absolute; left: 13px; top: 600px;
    color: var(--white);
    font-weight: 500;
    font-size: 16px;
    line-height: 25px;
    font-style: normal;
  }
  .contact .gap { margin-top: 10px; }
  .ad__footer {
    position: absolute; left: 0; right: 0; top: 750px; height: 98px;
    background: var(--orange);
    border-top: 3px solid var(--forest);
  }
  .ad__footer::before {
    content: ""; position: absolute; left: 0; right: 0; top: 5px; height: 3px;
    background: var(--forest);
  }
  .footer-name {
    position: absolute; right: 28px; top: 20px;
    color: var(--brown);
    font-weight: 600;
    font-size: 30px;
    line-height: 1;
    text-align: right;
  }
  .ad__base {
    position: absolute; left: 0; right: 0; bottom: 0; height: 18px;
    background: var(--forest);
    border-top: 4px solid var(--gold);
  }
</style>
</head>
<body>
  <article class="ad">
    <div class="ad__cap"></div>
    <header class="ad__header">
      <h1 class="brand-name">Brisley<br>Law Corporation</h1>
    </header>
    <div class="ad__photo" role="img" aria-label="Close-up photograph of a bald eagle's white head and yellow beak in profile against a blurred green background"></div>
    <p class="headline">
      Succesful <span class="accent">Trial</span><br>
      <span class="accent">Lawyers</span><br>
      <strong>Earn</strong> their <strong>Stripes</strong><br>
      In Court
    </p>
    <address class="contact">
      <div>Brisley Law Corporation</div>
      <div>388 Wexley Avenue, Suite 200</div>
      <div>Sacramento, CA 95871</div>
      <div class="gap">916.555.0147</div>
      <div>brisley-law.example</div>
    </address>
    <footer class="ad__footer">
      <p class="footer-name">Brisley<br>Law Corporation</p>
    </footer>
    <div class="ad__base"></div>
  </article>
</body>
</html>
```